law firm website

We need a website for our law firm that is based in Kabul, Afghanistan. We provide legal and government affairs services for the international community. We would like to see designs that use the colors of our logo, designs that are elegant and simple, yet not boring or over the top. No law or law related symbols or pictures. We would like clocks that show times for Kabul, Dubai and Washington DC.
Updates
Reason: No designs that are up to the task as yet. Perhaps we should stop using picture of people, that obviously don't work with us, in the website. If you are to use pictures, please try using pictures of Afghanistan mountains, art, craft etc. Also, please make the clocks very small - they seem to be dominating the website. We do not sell clocks or watches - we are a law firm. Hope you all understand and thank you for your designs to date.
Deal All,
Industry/Entity Type
Government
Requirements
Must have
- our logo.
the following phrases/words in flash.
"international standards" "local expertise" "integrity" "clarity" "commitment" "Afghanistan"
clocks: kabul, dubai, washington dc
Should not have
- law related pictures
afghanistan flag colors

```html
<!DOCTYPE html>
<html lang="en">
<head>
<meta charset="utf-8">
<title>Kestrel Counsel International</title>
<link rel="stylesheet" href="https://fonts.googleapis.com/css2?family=Cinzel:wght@400;600&family=Open+Sans:wght@400;600&display=swap">
<style>
  :root{
    --blue:#2a8fd0;
    --blue-light:#5fb3e6;
    --blue-dark:#1f6fa8;
    --ink:#3a3a3a;
    --muted:#6b6b6b;
    --paper:#ffffff;
    --rule:#d6d6d6;
    --card:#f4f4f4;
    --footer:#dadada;
    --magenta:#d8359c;
    --yellow:#f2c21b;
    --green:#5cbb3c;
  }
  *{box-sizing:border-box;margin:0;padding:0}
  html,body{width:700px;height:1200px;overflow:hidden}
  body{background:var(--paper);font-family:"Open Sans",Arial,sans-serif;color:var(--ink);position:relative}

  .site-header{position:relative;height:96px;display:flex;align-items:center;justify-content:center;gap:12px}
  .brand-mark{width:40px;height:40px;background:var(--ink);border-radius:50%}
  .brand-name{font-family:"Cinzel",Georgia,serif;font-size:18px;line-height:20px;color:var(--blue);letter-spacing:1px}

  .world-clocks{position:absolute;top:8px;right:14px;display:flex;gap:12px}
  .clock{display:flex;align-items:center;gap:4px;font-size:8px;line-height:10px;color:var(--muted)}
  .clock svg{width:14px;height:14px}
  .clock b{font-weight:600;color:var(--ink)}

  .main-nav{height:30px;background:linear-gradient(var(--blue-light),var(--blue));display:flex;align-items:center;padding-left:40px;gap:4px}
  .main-nav a{font-family:"Cinzel",Georgia,serif;font-size:10.5px;color:#fff;text-decoration:none;padding:4px 11px;letter-spacing:.5px}
  .main-nav a.is-active{background:#fff;color:var(--blue);border-radius:2px}

  .hero{position:relative;height:368px}
  .hero-photo{position:absolute;inset:0;background:linear-gradient(100deg,#c9cfd6 0%,#e8e2dc 35%,#d7dde3 60%,#8ea6bc 100%)}
  .hero-caption{position:absolute;left:0;right:0;bottom:0;height:58px;background:linear-gradient(rgba(20,30,45,0),rgba(20,30,45,.75));display:flex;align-items:center;padding-left:24px}
  .hero-caption h2{font-family:"Cinzel",Georgia,serif;font-weight:400;font-size:27px;color:#fff;letter-spacing:1.5px}
  .slider-dots{display:flex;justify-content:center;gap:6px;margin-top:9px}
  .slider-dots span{width:9px;height:9px;border-radius:50%;background:#c9d9e6}
  .slider-dots span.is-current{background:var(--blue)}

  .intro{padding:16px 22px 0}
  .intro-title{font-family:"Cinzel",Georgia,serif;font-weight:400;font-size:16px;line-height:22px;color:var(--ink)}
  .intro-title em{font-style:normal;color:var(--blue);font-size:19px}
  .intro-body{display:flex;gap:16px;margin-top:10px}
  .intro-text{flex:1;font-size:9.5px;line-height:14.5px;color:var(--muted)}
  .intro-text p{margin-bottom:3px}
  .intro-photo{width:256px;height:140px;margin-top:4px;border:3px solid #fff;box-shadow:0 0 3px rgba(0,0,0,.3);background:linear-gradient(135deg,#e9eef3,#b9c8d6 60%,#d9c8b6)}
  .btn{display:inline-block;background:var(--blue);color:#fff;font-size:8.5px;font-family:"Cinzel",Georgia,serif;padding:4px 16px;text-decoration:none;letter-spacing:.5px}
  .intro-more{text-align:right;margin-top:12px}

  .services{display:flex;gap:12px;padding:28px 14px 0}
  .service{flex:1;height:198px;background:var(--card);border:1px solid var(--rule);border-top:5px solid var(--blue);text-align:center;padding:12px 10px 12px;display:flex;flex-direction:column;align-items:center}
  .service.tax{border-top-color:var(--magenta)}
  .service.contracts{border-top-color:var(--yellow)}
  .service.projects{border-top-color:var(--green)}
  .service svg{width:30px;height:30px}
  .service h3{font-family:"Cinzel",Georgia,serif;font-weight:400;font-size:10.5px;line-height:13px;margin:10px 0 8px;color:var(--ink)}
  .service p{font-size:8px;line-height:12px;color:var(--muted);text-transform:uppercase}
  .service .btn{margin-top:auto}

  .site-footer{position:absolute;left:0;right:0;top:1000px;bottom:0;background:var(--footer);padding:16px 22px}
  .footer-row{display:flex;justify-content:space-between}
  .footer-label{font-family:"Cinzel",Georgia,serif;font-size:11px;color:var(--ink)}
  .footer-note{font-size:8.5px;line-height:12px;color:var(--muted);width:220px;margin-top:6px}
  .footer-address{font-family:"Cinzel",Georgia,serif;font-size:11px;margin-top:14px}
  .social{display:flex;gap:8px;margin-top:8px}
  .social span{width:34px;height:34px;background:var(--blue-dark)}
  .social span:nth-child(2){background:var(--blue-light)}
  .social span:nth-child(3){background:var(--blue)}
  .copyright{position:absolute;left:0;right:0;bottom:18px;text-align:center;font-size:9px;color:var(--muted)}
</style>
</head>
<body>
  <header class="site-header">
    <span class="brand-mark"></span>
    <span class="brand-name">Kestrel Counsel<br>International</span>
    <div class="world-clocks" aria-label="Local times">
      <span class="clock"><svg viewBox="0 0 14 14"><circle cx="7" cy="7" r="6" fill="none" stroke="#2a8fd0" stroke-width="1.2"/><path d="M7 3.5V7l2.5 1.5" fill="none" stroke="#3a3a3a" stroke-width="1"/></svg><span><b>Kabul</b> 14:30</span></span>
      <span class="clock"><svg viewBox="0 0 14 14"><circle cx="7" cy="7" r="6" fill="none" stroke="#2a8fd0" stroke-width="1.2"/><path d="M7 3.5V7l1.5 2.5" fill="none" stroke="#3a3a3a" stroke-width="1"/></svg><span><b>Dubai</b> 13:00</span></span>
      <span class="clock"><svg viewBox="0 0 14 14"><circle cx="7" cy="7" r="6" fill="none" stroke="#2a8fd0" stroke-width="1.2"/><path d="M7 3.5V7l-2.5 1" fill="none" stroke="#3a3a3a" stroke-width="1"/></svg><span><b>Washington DC</b> 05:00</span></span>
    </div>
  </header>

  <nav class="main-nav">
    <a class="is-active" href="#">Home</a>
    <a href="#">About The Firm</a>
    <a href="#">Our Lawyers ▾</a>
    <a href="#">Services</a>
    <a href="#">Ethics</a>
    <a href="#">Publication</a>
    <a href="#">Trainings</a>
  </nav>

  <section class="hero">
    <div class="hero-photo" role="img" aria-label="Photograph of the firm's team of lawyers"></div>
    <div class="hero-caption"><h2>International Standards</h2></div>
  </section>
  <div class="slider-dots"><span class="is-current"></span><span></span><span></span><span></span><span></span></div>

  <section class="intro">
    <h1 class="intro-title">We strive to be <em>attentive</em>, <em>diligent</em>, and <em>successful</em> for each client that walks into our law office.</h1>
    <div class="intro-body">
      <div class="intro-text">
        <p>We are an independent legal and government relations advisory firm staffed by experienced lawyers from Kabul, the Gulf and North America.</p>
        <p>We provide practical legal, regulatory, tax and government relations advice to development agencies, institutions, businesses, investors and public bodies.</p>
        <p>We are known for our commercial approach and our honesty. We frequently represent clients on complex and significant matters and transactions.</p>
        <div class="intro-more"><a class="btn" href="#">Read more...</a></div>
      </div>
      <div class="intro-photo" role="img" aria-label="Photograph of a smiling client with an adviser"></div>
    </div>
  </section>

  <section class="services">
    <article class="service corporate">
      <svg viewBox="0 0 32 32"><circle cx="16" cy="16" r="11" fill="none" stroke="#555" stroke-width="2"/><path d="M16 9v14M12 13h6a2 2 0 0 1 0 4h-4a2 2 0 0 0 0 4h6" fill="none" stroke="#555" stroke-width="1.6"/></svg>
      <h3>Corporate and Investment</h3>
      <p>Specific and integrated legal services to organisations doing business, and overseas investors looking to set up a base in the region.</p>
      <a class="btn" href="#">Read more...</a>
    </article>
    <article class="service tax">
      <svg viewBox="0 0 32 32"><rect x="8" y="4" width="16" height="24" rx="2" fill="none" stroke="#555" stroke-width="2"/><rect x="11" y="7" width="10" height="5" fill="#555"/><g fill="#555"><rect x="11" y="15" width="3" height="3"/><rect x="15" y="15" width="3" height="3"/><rect x="19" y="15" width="2" height="3"/><rect x="11" y="20" width="3" height="3"/><rect x="15" y="20" width="3" height="3"/><rect x="19" y="20" width="2" height="3"/></g></svg>
      <h3>Tax</h3>
      <p>The firm specialises in the full range of tax issues such as exemptions, withholding taxes, corporate income tax and customs duties.</p>
      <a class="btn" href="#">Read more...</a>
    </article>
    <article class="service contracts">
      <svg viewBox="0 0 32 32"><rect x="8" y="4" width="16" height="24" fill="none" stroke="#555" stroke-width="2"/><path d="M12 10h8M12 14h8M12 18h8M12 22h5" stroke="#555" stroke-width="1.6"/></svg>
      <h3>Commercial contracts</h3>
      <p>Broad practice encompassing a range of commercial contracts and joint ventures, together with agency, distribution and franchising work.</p>
      <a class="btn" href="#">Read more...</a>
    </article>
    <article class="service projects">
      <svg viewBox="0 0 32 32"><path d="M5 27h22" stroke="#555" stroke-width="2"/><rect x="8" y="17" width="4" height="10" fill="#555"/><rect x="14" y="12" width="4" height="15" fill="#555"/><rect x="20" y="7" width="4" height="20" fill="#555"/></svg>
      <h3>Projects</h3>
      <p>Providing local counsel support for large and complex projects across a range of industries, including mining and infrastructure.</p>
      <a class="btn" href="#">Read more...</a>
    </article>
  </section>

  <footer class="site-footer">
    <div class="footer-row">
      <div>
        <div class="footer-label">Postal Address</div>
        <p class="footer-note">Our chambers welcome visitors by appointment. Please write to the address below for all formal correspondence.</p>
        <p class="footer-address">4120 Orchard Lane, Harwick.</p>
      </div>
      <div>
        <div class="footer-label">Follow us:</div>
        <div class="social" aria-label="Social channels"><span></span><span></span><span></span></div>
      </div>
    </div>
    <p class="copyright">Copyright © 2013 | All Right Reserved</p>
  </footer>
</body>
</html>
```